Brindle painting & waterproofing business card.

Business cards updated to reflect photos attached. we have given the photos of the old business cards and some of our updated designs for other items we have here in the office. Please see attached. if anyone needs to contact us directly for clarification you can email us at brindlerestoration@mailvane.com

Industry/Entity Type

Construction

Contact Information for Business Card

See attached photos

Font styles to use
Other font styles liked:
• Same as photos

Colors
ec1f27

Requirements
Must have
• Employee Names,
• Gordon Brindle II, Supervisor/Owner
• Gord Brindle, President/Owner
• Tim Harker, Sales Representative
• Lou Marsten, Supervisor
• Change 20 years to 25
Nice to have
• ideas reflecting the attached photos
Should not have
• should not be exactly like attached photos as those are old business card but reflect to match new logo listed as kelvar van and cup photo.

```html
<!DOCTYPE html>
<html lang="en">
<head>
<meta charset="utf-8">
<title>Brindle's Painting &amp; Restoration – Business Card</title>
<link href="https://fonts.googleapis.com/css2?family=Lato:wght@400;700;900&display=swap" rel="stylesheet">
<style>
  :root {
    --brand-red: #ec1f27;
    --deep-red: #a3141b;
    --dark-red: #7d0e13;
    --ink: #2b2b2b;
    --charcoal: #111;
    --paper: #ffffff;
    --backdrop: #d6d6d6;
  }
  * { margin: 0; padding: 0; box-sizing: border-box; }
  html, body { width: 1200px; height: 900px; overflow: hidden; }
  body {
    background: var(--backdrop);
    font-family: "Lato", sans-serif;
    position: relative;
  }
  .card {
    position: absolute;
    left: 280px;
    width: 640px;
    height: 366px;
    overflow: hidden;
    box-shadow: 0 6px 18px rgba(0,0,0,.18);
  }
  .card-front { top: 59px; background: var(--brand-red); }
  .card-back { top: 475px; background: var(--paper); }
  .card-art { position: absolute; inset: 0; width: 100%; height: 100%; }

  /* Front */
  .front-brand {
    position: absolute; left: 90px; top: 46px; width: 460px;
    text-align: center; color: var(--paper);
    font-weight: 900; text-transform: uppercase; line-height: 1;
  }
  .front-brand .brand-main { display: block; font-size: 50px; letter-spacing: 3px; }
  .front-brand .brand-sub { display: block; font-size: 22px; letter-spacing: 5px; margin-top: 8px; }
  .anniversary-mark {
    position: absolute; left: 290px; top: 150px; width: 60px; height: 44px;
    border-radius: 50%;
    background: radial-gradient(circle, rgba(255,255,255,.55), rgba(255,255,255,.15));
  }
  .services {
    position: absolute; left: 40px; right: 40px; top: 212px;
    text-align: center; color: var(--paper);
    font-size: 15px; line-height: 1.45;
  }
  .services .services-lead { font-weight: 700; font-size: 16px; }
  .front-web {
    position: absolute; left: 0; right: 0; bottom: 24px;
    text-align: center; color: var(--paper); font-weight: 700; font-size: 16px;
  }

  /* Back */
  .back-brand {
    position: absolute; left: 34px; top: 30px;
    color: var(--brand-red); font-weight: 900; text-transform: uppercase; line-height: 1;
  }
  .back-brand .brand-main { display: block; font-size: 40px; letter-spacing: 2px; }
  .back-brand .brand-sub { display: block; font-size: 16px; letter-spacing: 3px; margin-top: 7px; }
  .person {
    position: absolute; right: 176px; top: 112px; text-align: right;
  }
  .person-name { font-weight: 900; font-size: 21px; color: var(--ink); letter-spacing: .3px; line-height: 1.1; }
  .person-title { font-size: 14px; color: var(--ink); margin-top: 3px; }
  .contact {
    position: absolute; left: 34px; top: 170px;
    list-style: none; color: var(--ink); font-size: 14px; line-height: 1.55;
  }
  .contact li { display: flex; align-items: center; gap: 7px; }
  .contact svg { width: 12px; height: 12px; flex: none; }
  .credentials {
    position: absolute; right: 26px; bottom: 30px;
    text-align: right; color: var(--paper); font-size: 15px; line-height: 1.35;
  }
</style>
</head>
<body>

<section class="card card-front">
  <svg class="card-art" viewBox="0 0 640 366" preserveAspectRatio="none" aria-hidden="true">
    <defs>
      <linearGradient id="frontBase" x1="0" y1="0" x2="1" y2="1">
        <stop offset="0" stop-color="#ec1f27"/>
        <stop offset=".55" stop-color="#c8161e"/>
        <stop offset="1" stop-color="#8e1016"/>
      </linearGradient>
      <radialGradient id="frontGlow" cx=".7" cy=".45" r=".6">
        <stop offset="0" stop-color="#ff4a50" stop-opacity=".45"/>
        <stop offset="1" stop-color="#ff4a50" stop-opacity="0"/>
      </radialGradient>
    </defs>
    <rect width="640" height="366" fill="url(#frontBase)"/>
    <rect width="640" height="366" fill="url(#frontGlow)"/>
    <path d="M0 40 C 200 60, 380 200, 430 366 L 380 366 C 330 220, 170 90, 0 70 Z" fill="#ffffff" opacity=".08"/>
    <path d="M0 110 C 180 130, 300 240, 320 366 L 290 366 C 260 250, 150 150, 0 140 Z" fill="#000" opacity=".08"/>
    <path d="M420 0 C 470 120, 470 250, 430 366" stroke="#ffffff" stroke-opacity=".12" stroke-width="14" fill="none"/>
  </svg>

  <div class="front-brand">
    <span class="brand-main">Brindle's</span>
    <span class="brand-sub">Painting &amp; Restoration</span>
  </div>
  <div class="anniversary-mark" role="img" aria-label="Hand-lettered 25 years anniversary mark"></div>

  <div class="services">
    <p class="services-lead">Specializing in Hi-rises &amp; Commercial</p>
    <p>Concrete Restoration | Waterproofing | Painting | Electrostatic</p>
    <p>Expansion Joints | Caulking | Deck Coatings | Balustrades &amp; Railings</p>
  </div>
  <p class="front-web">www.brindlerestoration.com</p>
</section>

<section class="card card-back">
  <svg class="card-art" viewBox="0 0 640 366" preserveAspectRatio="none" aria-hidden="true">
    <defs>
      <linearGradient id="bandRed" x1="0" y1="0" x2="1" y2="1">
        <stop offset="0" stop-color="#ec1f27"/>
        <stop offset="1" stop-color="#a3141b"/>
      </linearGradient>
    </defs>
    <path d="M508 0 C 500 170, 420 300, 250 366 L 640 366 L 640 0 Z" fill="#111"/>
    <path d="M520 0 C 514 170, 440 300, 268 366 L 640 366 L 640 0 Z" fill="url(#bandRed)"/>
  </svg>

  <div class="back-brand">
    <span class="brand-main">Brindle's</span>
    <span class="brand-sub">Painting &amp; Restoration</span>
  </div>

  <div class="person">
    <p class="person-name">GORDON BRINDLE II</p>
    <p class="person-title">Supervisor / Owner</p>
  </div>

  <ul class="contact">
    <li>2140 NE 31st Ave.</li>
    <li>Harbor BCH, FL 33069</li>
    <li>
      <svg viewBox="0 0 14 14"><rect x="3" y="1" width="8" height="12" rx="1.5" fill="none" stroke="#ec1f27" stroke-width="1.5"/></svg>
      954-555-0148
    </li>
    <li>
      <svg viewBox="0 0 14 14"><path d="M3 1 L5.5 1 L6.5 4 L5 5.2 C5.8 7 7 8.2 8.8 9 L10 7.5 L13 8.5 L13 11 C13 12 12 13 11 13 C6 12.5 1.5 8 1 3 C1 2 2 1 3 1 Z" fill="#ec1f27"/></svg>
      954-555-0172
    </li>
    <li>
      <svg viewBox="0 0 14 14"><rect x="1" y="3" width="12" height="8" fill="none" stroke="#ec1f27" stroke-width="1.5"/><path d="M1 3 L7 8 L13 3" fill="none" stroke="#ec1f27" stroke-width="1.5"/></svg>
      brindlerestoration@mailvane.com
    </li>
    <li>
      <svg viewBox="0 0 14 14"><circle cx="7" cy="7" r="6" fill="none" stroke="#ec1f27" stroke-width="1.4"/><ellipse cx="7" cy="7" rx="2.6" ry="6" fill="none" stroke="#ec1f27" stroke-width="1.1"/><path d="M1 7 H13" stroke="#ec1f27" stroke-width="1.1"/></svg>
      www.brindlerestoration.com
    </li>
  </ul>

  <div class="credentials">
    <p>General Contractor</p>
    <p>CGC#1508264</p>
    <p>LICENSED &amp; INSURED</p>
  </div>
</section>

</body>
</html>
```